"ZENTRAL BEAT" - German Rap Concert

Hello,

I need a Flyer for a concert in Reutlingen, Germany.
The following Information should be included in the Flyer:

"ZENTRAL BEAT

09.01.2015
Beginn: 17:00 Uhr
Einlass: 15:30 Uhr

Acts:
OLU MARVIN
Rune Saly
Lomberg & SkyeNoBoy
PIM
Dorvin. KLU & Santo
BlueTrack

VVK: 26€

Klangwerk, Ferdinandstr. 14, 72760 Reutlingen"

The Logo of the Location should also be in the Flyer.
Main Act is Olu Marvin. you can find a Picture of him attached.
We also need space for Sponsoring-logos (4) at the bottom of the Flyer.
The Logos of the Sponsors will come later.

I hope you can understand my english ;)
If you have any questions, just write me an email.

Thanks in advance!

Tobias

Edit: The size of the Flyer should be DinA6.
I have also uploaded a better Version of the Klangwerk Logo!

Dear Designers, I have uploaded 3 of the 4 Sponsoring-Logos. Please insert them into the Flyer! Sponsors: RTV-P (please write under the logo "Sport- & Eventmanagement") Falk Brauerei Wendlinger Thanks!

```html
<!DOCTYPE html>
<html lang="de">
<head>
<meta charset="utf-8">
<title>ZENTRAL BEAT – Flyer</title>
<link rel="stylesheet" href="https://fonts.googleapis.com/css2?family=Anton&family=Oswald:wght@500;700&family=Great+Vibes&display=swap">
<style>
  :root {
    --orange-deep: #b33a06;
    --orange: #e36a0f;
    --orange-light: #f7a21c;
    --panel: #4a4a4c;
    --panel-dark: #2c2c2e;
    --yellow: #f3ec58;
    --yellow-pale: #ece98a;
    --gold: #f5c400;
    --maroon: #6e0d0d;
    --white: #ffffff;
    --ink: #2a2a2a;
    --green: #3f8f3a;
    --navy: #1f2a44;
    --sky: #d5e8f4;
  }
  * { margin: 0; padding: 0; box-sizing: border-box; }
  html, body { width: 846px; height: 1200px; overflow: hidden; background: #ccc; }
  .flyer {
    position: relative; width: 846px; height: 1200px; overflow: hidden;
    background: radial-gradient(ellipse at 35% 30%, var(--orange-light) 0%, var(--orange) 45%, var(--orange-deep) 100%);
    font-family: "Oswald", sans-serif;
  }
  .title-panel {
    position: absolute; left: 60px; top: 40px; width: 730px; height: 560px;
    background: linear-gradient(160deg, var(--panel) 0%, var(--panel-dark) 100%);
    clip-path: polygon(0 0, 100% 0, 100% 60%, 0 100%);
    opacity: .9;
  }
  .title-main {
    position: absolute; left: 0; right: 0; top: 28px; text-align: center;
    font-family: "Anton", sans-serif; font-size: 150px; line-height: 1; letter-spacing: 2px;
    color: var(--orange-light);
    background: linear-gradient(180deg, #fff 0%, #fff 40%, var(--orange-light) 45%, var(--orange) 100%);
    -webkit-background-clip: text; background-clip: text; -webkit-text-fill-color: transparent;
  }
  .title-script {
    position: absolute; left: 170px; top: 170px;
    font-family: "Great Vibes", cursive; font-size: 140px; line-height: 1;
    color: #f2e6e6; text-shadow: 2px 3px 4px rgba(0,0,0,.5);
  }
  .artist-photo {
    position: absolute; left: 380px; top: 210px; width: 466px; height: 520px;
    background: radial-gradient(ellipse at 55% 40%, #c99a7a 0%, #6f4a38 45%, rgba(60,40,30,0) 75%);
  }
  .date-badge { position: absolute; left: 78px; top: 345px; width: 250px; height: 250px; }
  .date-text {
    position: absolute; left: 78px; top: 410px; width: 250px; text-align: center; color: var(--panel-dark);
  }
  .date-day { font-family: "Anton", sans-serif; font-size: 40px; line-height: 1; }
  .date-num { font-family: "Anton", sans-serif; font-size: 78px; line-height: .95; color: #444; }
  .date-month { font-family: "Anton", sans-serif; font-size: 38px; line-height: 1; color: #111; }
  .date-year { font-family: "Oswald", sans-serif; font-weight: 700; font-size: 16px; color: #9a6a00; }
  .lower-band { position: absolute; left: 0; top: 690px; width: 846px; height: 430px; }
  .headliner {
    position: absolute; left: 155px; top: 668px; width: 540px; height: 125px;
    background: var(--yellow); transform: rotate(-2deg);
    display: flex; align-items: center; justify-content: center;
    box-shadow: 0 4px 10px rgba(0,0,0,.35);
  }
  .headliner span {
    font-family: "Anton", sans-serif; font-size: 96px; line-height: 1; color: var(--maroon);
    transform: scaleY(1.15);
  }
  .support-label {
    position: absolute; left: 0; right: 0; top: 796px; text-align: center;
    font-weight: 700; font-size: 16px; letter-spacing: 7px; color: var(--gold);
  }
  .support-acts {
    position: absolute; left: 0; right: 0; top: 812px; text-align: center;
    font-family: "Oswald", sans-serif; font-weight: 700; font-size: 33px; line-height: 1.12;
    color: var(--white); text-transform: uppercase; text-shadow: 1px 2px 3px rgba(0,0,0,.5);
  }
  .support-acts .hl { color: var(--gold); }
  .info-bar {
    position: absolute; left: 90px; top: 893px; width: 660px; height: 26px;
    background: var(--ink); transform: rotate(-1deg);
    color: var(--yellow); font-weight: 700; font-size: 18px; line-height: 26px; text-align: center;
    letter-spacing: .5px;
  }
  .venue-logo {
    position: absolute; left: 0; right: 0; top: 942px; text-align: center;
    font-family: "Anton", sans-serif; font-size: 66px; line-height: 1; color: var(--ink); letter-spacing: 1px;
  }
  .venue-sub {
    position: absolute; left: 420px; top: 1016px; font-size: 11px; letter-spacing: 1.5px; color: var(--ink);
  }
  .venue-address {
    position: absolute; left: 0; right: 0; top: 1046px; text-align: center;
    font-weight: 700; font-size: 22px; letter-spacing: 2px; color: var(--ink);
    border-top: 2px dotted var(--ink); width: 470px; margin: 0 auto; padding-top: 6px;
  }
  .sponsor-strip {
    position: absolute; left: 0; top: 1110px; width: 846px; height: 90px;
    background: linear-gradient(180deg, #eef6fb, var(--sky));
  }
  .sponsor-center {
    position: absolute; left: 225px; top: 1110px; width: 395px; height: 90px;
    background: var(--navy); clip-path: polygon(10% 0, 90% 0, 100% 100%, 0 100%);
  }
  .sponsor {
    position: absolute; top: 1110px; height: 90px; display: flex; align-items: center; justify-content: center; gap: 8px;
    font-family: "Oswald", sans-serif; font-weight: 700;
  }
  .sponsor-left { left: 40px; width: 150px; color: var(--ink); font-size: 22px; }
  .sponsor-mid { left: 260px; width: 325px; color: var(--white); font-size: 32px; letter-spacing: 1px; }
  .sponsor-right { left: 660px; width: 170px; }
  .sponsor-badge { width: 70px; height: 70px; border-radius: 50%; background: #8a8f94; }
  .sponsor-dot { width: 14px; height: 14px; border-radius: 50%; background: var(--ink); }
</style>
</head>
<body>
<div class="flyer">
  <div class="title-panel"></div>
  <div class="artist-photo" role="img" aria-label="Portrait photo of headliner Olu Marvin wearing sunglasses, lit in warm orange"></div>

  <h1 class="title-main">ZENTRAL</h1>
  <div class="title-script">Beat</div>

  <svg class="date-badge" viewBox="0 0 250 250" aria-hidden="true">
    <circle cx="125" cy="125" r="122" fill="none" stroke="#f5c400" stroke-width="8" stroke-dasharray="2 3"/>
    <circle cx="125" cy="125" r="108" fill="#c98a00"/>
    <circle cx="125" cy="125" r="100" fill="#f3ec58"/>
    <circle cx="125" cy="125" r="100" fill="none" stroke="#fff6a0" stroke-width="3"/>
  </svg>
  <div class="date-text">
    <div class="date-day">Freitag</div>
    <div class="date-num">09</div>
    <div class="date-month">JANUAR</div>
    <div class="date-year">2015</div>
  </div>

  <svg class="lower-band" viewBox="0 0 846 430" preserveAspectRatio="none" aria-hidden="true">
    <path d="M0 150 Q300 100 560 160 Q720 200 846 60 L846 430 L0 430 Z" fill="#ece98a"/>
    <path d="M0 150 Q300 100 560 160 Q720 200 846 60 L846 80 Q720 215 560 178 Q300 120 0 168 Z" fill="#f3ec58"/>
  </svg>

  <div class="headliner"><span>OLU MARVIN</span></div>
  <div class="support-label">SUPPORTING ACTS</div>
  <div class="support-acts">
    Rune <span class="hl">Saly</span> / Lomberg <span class="hl">&amp; SkyeNoBoy</span> / PIM<br>
    Dorvin. KLU <span class="hl">&amp; Santo</span> / <span class="hl">Blue</span>Track
  </div>
  <div class="info-bar">VVK: 26€ // BEGINN: 17:00 UHR - EINLASS: 15:30 UHR</div>

  <div class="venue-logo">KLANGWERK</div>
  <div class="venue-sub">BILLARD · SPORTSBAR · LOUNGE</div>
  <div class="venue-address">FERDINANDSTR. 14, 72760 REUTLINGEN</div>

  <div class="sponsor-strip"></div>
  <div class="sponsor-center"></div>
  <div class="sponsor sponsor-left"><span class="sponsor-dot"></span>RTV-P</div>
  <div class="sponsor sponsor-mid">Wendlinger</div>
  <div class="sponsor sponsor-right"><span class="sponsor-badge" role="img" aria-label="Falk Brauerei sponsor badge"></span></div>
</div>
</body>
</html>
```